Brightpath Works Mobile RV Repair

We are looking for a logo and business cards for a new start up business. We will be doing Mobile RV Repair.
We are in Texas.
I don't have any designs at this point.

Contact Information for Business Card

Emphasis should be on the “Mobile RV Repair” and not so much the name “Brightpath Works”

Requirements
Nice to have
• I like the Mobile RV Repair to cover most of the backside of the card! Not sure on the colors, would like to see it in a few different colors!

```html
<!DOCTYPE html>
<html lang="en">
<head>
<meta charset="utf-8">
<title>Brightpath Works – Business Card</title>
<link rel="stylesheet" href="https://fonts.googleapis.com/css2?family=Bebas+Neue&family=Oswald:wght@500&family=Lato:wght@400&display=swap">
<style>
  :root {
    --gold: #e1a617;
    --ink: #111111;
    --paper: #ffffff;
    --rule: #8a8a8a;
    --backdrop: #a9a9a9;
  }
  * { margin: 0; padding: 0; box-sizing: border-box; }
  html, body {
    width: 1200px; height: 1200px; overflow: hidden;
    background: var(--backdrop);
  }
  .canvas { position: relative; width: 1200px; height: 1200px; }

  .card {
    position: absolute; top: 304px; width: 362px; height: 594px;
    border-radius: 26px;
  }

  /* Back side: service line fills most of the card */
  .card-back {
    left: 203px;
    background: var(--gold);
    border: 5px solid var(--ink);
    border-left-width: 4px;
    display: flex; flex-direction: column;
    align-items: center; justify-content: center;
    font-family: "Bebas Neue", sans-serif;
    color: var(--ink);
    text-align: center;
  }
  .back-name {
    font-size: 34px; line-height: 1; letter-spacing: 3px;
    margin-bottom: 22px;
  }
  .back-service {
    font-size: 118px; line-height: 0.92; letter-spacing: 2px;
  }

  /* Front side */
  .card-front {
    left: 600px;
    background: var(--paper);
    border-radius: 10px;
    text-align: center;
    color: var(--ink);
  }
  .brand-dot {
    position: absolute; left: 121px; top: 66px;
    width: 120px; height: 120px; border-radius: 50%;
    background: var(--gold);
  }
  .brand-name-front {
    position: absolute; left: 0; right: 0; top: 238px;
    font-family: "Bebas Neue", sans-serif; font-weight: 400;
    font-size: 46px; line-height: 1; color: var(--ink);
  }
  .tagline {
    position: absolute; left: 52px; right: 52px; top: 284px;
    display: flex; align-items: center; gap: 8px;
    font-family: "Oswald", sans-serif; font-weight: 500;
    font-size: 15px; line-height: 1; letter-spacing: 4px; color: var(--gold);
    white-space: nowrap;
  }
  .tagline::before, .tagline::after {
    content: ""; flex: 1; height: 1px; background: var(--gold);
  }
  .person-name {
    position: absolute; left: 0; right: 0; top: 338px;
    font-family: "Bebas Neue", sans-serif; font-weight: 400;
    font-size: 36px; line-height: 1; color: var(--gold);
  }
  .person-role {
    position: absolute; left: 0; right: 0; top: 372px;
    font-family: "Lato", sans-serif; font-size: 17px; line-height: 22px;
  }
  .contact-icons {
    position: absolute; left: 86px; right: 86px; top: 400px;
    display: flex; align-items: center; gap: 4px;
  }
  .contact-icons .line { flex: 1; height: 1px; background: var(--rule); }
  .contact-icons .icon {
    width: 25px; height: 25px; border-radius: 3px;
    background: var(--gold);
    display: flex; align-items: center; justify-content: center;
  }
  .contact-list {
    position: absolute; left: 0; right: 0; top: 436px;
    font-family: "Lato", sans-serif; font-size: 17px; line-height: 22px;
  }
  .contact-list .accent { color: var(--gold); }
  .divider {
    position: absolute; left: 88px; right: 80px; top: 511px;
    height: 1px; background: var(--rule);
  }
  .address {
    position: absolute; left: 0; right: 0; top: 519px;
    font-family: "Lato", sans-serif; font-size: 17px; line-height: 22px;
  }
</style>
</head>
<body>
<main class="canvas">

  <section class="card card-back" aria-label="Business card back">
    <p class="back-name">Brightpath Works</p>
    <p class="back-service">Mobile<br>RV<br>Repair</p>
  </section>

  <section class="card card-front" aria-label="Business card front">
    <div class="brand-dot" aria-hidden="true"></div>
    <h1 class="brand-name-front">BRIGHTPATH WORKS</h1>
    <p class="tagline">MOBILE RV REPAIR</p>

    <h2 class="person-name">DANIEL REYES</h2>
    <p class="person-role">Managing Director</p>

    <div class="contact-icons">
      <span class="line"></span>
      <span class="icon" aria-label="Phone">
        <svg width="15" height="15" viewBox="0 0 24 24" fill="#fff"><path d="M6.6 10.8a15 15 0 0 0 6.6 6.6l2.2-2.2a1 1 0 0 1 1-.25 11.4 11.4 0 0 0 3.6.57 1 1 0 0 1 1 1V20a1 1 0 0 1-1 1A17 17 0 0 1 3 4a1 1 0 0 1 1-1h3.5a1 1 0 0 1 1 1c0 1.25.2 2.45.57 3.6a1 1 0 0 1-.25 1z"/></svg>
      </span>
      <span class="icon" aria-label="Email">
        <svg width="16" height="12" viewBox="0 0 16 12" fill="none" stroke="#fff" stroke-width="1.2"><rect x="0.6" y="0.6" width="14.8" height="10.8"/><path d="M0.6 0.6 8 7l7.4-6.4M0.6 11.4l5.4-5.6M15.4 11.4 10 5.8"/></svg>
      </span>
      <span class="icon" aria-label="Website">
        <svg width="15" height="15" viewBox="0 0 16 16" fill="none" stroke="#fff" stroke-width="1.3"><circle cx="8" cy="8" r="6.6"/><path d="M1.4 8h13.2M8 1.4c2 2 2 11.2 0 13.2M8 1.4c-2 2-2 11.2 0 13.2"/></svg>
      </span>
      <span class="line"></span>
    </div>

    <p class="contact-list">
      044-555 210 348<br>
      info@brightpathworks.com<br>
      www.<span class="accent">brightpathworks</span>.com
    </p>
    <div class="divider"></div>
    <p class="address">
      218 Mesquite Road<br>
      78701, Texas
    </p>
  </section>

</main>
</body>
</html>
```